Rock band business card design

I need an edgy double sided business card to hand out at music events and to send out to radio.

It needs to display our logo, web address and social media icons (linkora, plumbit, vostramesh).

Colour scheme to match our website (www.thedrelliq.com)

Please include this quote:
The clock is turning... a reckoning... THE DRELLIQ.

Logo files have been attached.

I look forward to seeing your designs!

Target Market(s)

radio stations, music fans.

Industry/Entity Type

Events

Requirements
Must have
• Website address, social media icons, quote, colour scheme to match www.thedrelliq.com

```html
<!DOCTYPE html>
<html lang="en">
<head>
<meta charset="utf-8">
<title>The Drelliq – Business Card</title>
<link rel="stylesheet" href="https://fonts.googleapis.com/css2?family=Cinzel:wght@600;700&family=Arimo:wght@400;700&display=swap">
<style>
  :root {
    --backdrop: #2b2b2b;
    --parchment: #e9e3b4;
    --parchment-shade: #d9d09a;
    --ink: #111111;
    --gold: #e0a21c;
    --gold-light: #f6cf5a;
    --gold-dark: #9a6410;
    --genre-edge: #3a2a05;
    --band-grey: #6f6f6f;
    --sand: #c9a66a;
    --sand-dark: #a9844c;
    --rule: #3a3a3a;
  }
  * { box-sizing: border-box; margin: 0; padding: 0; }
  html, body {
    width: 1200px; height: 863px; overflow: hidden;
    background: var(--backdrop);
  }
  .canvas {
    width: 1200px; height: 863px;
    display: flex; align-items: center; justify-content: center; gap: 40px;
  }
  .card {
    position: relative;
    width: 560px; height: 320px;
    background: radial-gradient(ellipse at 40% 40%, var(--parchment) 0%, var(--parchment) 55%, var(--parchment-shade) 100%);
    overflow: hidden;
    font-family: "Arimo", Arial, sans-serif;
    color: var(--ink);
  }

  /* Front */
  .gold-band {
    position: absolute; left: 0; right: 0; height: 12px;
    background: linear-gradient(90deg, var(--gold-dark), var(--gold-light) 25%, var(--gold) 50%, var(--gold-light) 75%, var(--gold-dark));
  }
  .gold-band::after {
    content: ""; position: absolute; left: 0; right: 0; height: 4px;
    background: var(--band-grey);
  }
  .gold-band--top { top: 26px; }
  .gold-band--top::after { bottom: -6px; }
  .gold-band--bottom { bottom: 26px; }
  .gold-band--bottom::after { top: -6px; }

  .band-name {
    font-family: "Cinzel", Georgia, serif;
    font-weight: 700;
    color: var(--ink);
    letter-spacing: 1px;
  }
  .front .band-name {
    position: absolute; top: 78px; left: 0; right: 0;
    text-align: center; font-size: 34px;
  }
  .emblem-mark {
    position: absolute; top: 132px; left: 50%;
    width: 26px; height: 26px; margin-left: -13px;
    background: var(--ink);
  }
  .front .quote {
    position: absolute; top: 218px; left: 0; right: 0;
    text-align: center; font-size: 14px;
  }

  /* Back */
  .desert-scene {
    position: absolute; top: 0; left: 0; right: 0; height: 110px;
    background: linear-gradient(180deg, var(--parchment) 0%, var(--sand) 60%, var(--sand-dark) 100%);
    opacity: .75;
  }
  .back .band-name {
    position: absolute; top: 12px; left: 0; right: 0;
    text-align: center; font-size: 28px;
  }
  .back .emblem-mark { top: 56px; width: 22px; height: 22px; margin-left: -11px; }
  .back .quote--upper {
    position: absolute; top: 88px; right: 24px;
    font-size: 12px;
  }
  .divider {
    position: absolute; left: 24px; right: 24px; height: 1px; background: var(--rule);
  }
  .divider--upper { top: 110px; }
  .divider--lower { top: 226px; }
  .genre {
    position: absolute; top: 118px; left: 24px;
    font-weight: 700; font-size: 16px; color: var(--gold);
    text-shadow: 1px 1px 0 var(--genre-edge), -1px -1px 0 var(--genre-edge),
                 1px -1px 0 var(--genre-edge), -1px 1px 0 var(--genre-edge);
  }
  .back .quote--lower {
    position: absolute; top: 146px; left: 0; right: 0;
    text-align: center; font-size: 15px;
  }
  .links {
    position: absolute; font-size: 12px; font-weight: 700; list-style: none;
  }
  .links li { display: flex; align-items: center; gap: 8px; height: 22px; }
  .links .marker {
    width: 16px; height: 16px; background: var(--rule); flex: none;
  }
  .links--music { right: 24px; top: 174px; }
  .links--social { left: 24px; top: 238px; }
  .website {
    position: absolute; right: 40px; top: 250px;
    font-size: 16px; font-weight: 700;
  }
</style>
</head>
<body>
<main class="canvas">

  <section class="card front" aria-label="Card front">
    <div class="gold-band gold-band--top"></div>
    <h1 class="band-name">THE DRELLIQ</h1>
    <div class="emblem-mark"></div>
    <p class="quote">The clock is turning... a reckoning... THE DRELLIQ.</p>
    <div class="gold-band gold-band--bottom"></div>
  </section>

  <section class="card back" aria-label="Card back">
    <div class="desert-scene" role="img" aria-label="Desert landscape with pyramids in sandy tones"></div>
    <h2 class="band-name">THE DRELLIQ</h2>
    <div class="emblem-mark"></div>
    <p class="quote quote--upper">The clock is turning... a reckoning... THE DRELLIQ.</p>
    <div class="divider divider--upper"></div>
    <p class="genre">Rock / Melodic Rock / Experimental</p>
    <p class="quote quote--lower">The clock is turning... a reckoning... THE DRELLIQ.</p>
    <ul class="links links--music">
      <li><span class="marker"></span>http://www.vostramesh.com/thedrelliq</li>
      <li><span class="marker"></span>http://thedrelliq.tunestall.com</li>
    </ul>
    <div class="divider divider--lower"></div>
    <ul class="links links--social">
      <li><span class="marker"></span>https://www.linkora.com/thedrelliq</li>
      <li><span class="marker"></span>https://plumbit.com/thedrelliq</li>
    </ul>
    <p class="website">www.thedrelliq.com</p>
  </section>

</main>
</body>
</html>
```